Product Label Design

We require 2 labels, with the same look and feel, designed for our range of trucking related products for the transport industry. Our logo has been provided.

In terms of the look and feel, we are after:
- a clean and elegant design to represent our premium range of products. By clean we mean not "too busy" or cluttered
- masculine as this relates to trucking,
- must convey that our products are cutting-edge and innovative (our competitors' labels are outdated and dull thus we want to stand-out in the world market)

We want you to create a standardised label template for us, which we can use for several products. We will simply change the product description and product code and reprint.

Each product label will have a:
• Product Description
• Product code
• An image or artwork of a truck as all our products are for the transport industry
• Display product Size in bottom right hand corner
Label 1: 20L (180 mm x 180 mm with 5 mm radius on corners )
Label 2: 750ml (A copy of the 750ml bottle die line has been unloaded as a PDF)

You may use text placeholders for the description.

Files Required:
We need the final design as a psd file, as our business uses Photoshop CS6.

REFERENCE:
Attached is an sample label with the features we want (ie product description, product size, and so on). Please DO NOT use or see this as a reference for your design or style we are after. We do not want your creativity to be restricted by this sample.

Target Market(s)

Products for the trucking industry

Industry/Entity Type

Industry

Colors

Designer to choose colors to be used in the design.

Requirements
Must have
• Logo
• • Image of a truck on the label (preferably the truck should be cutting edge and modern to align it with our product)
• • Some type of background
• • Product description
• • Product code
• • Product size on Bottom Right corner
Should not have
• Unnecessary graphics that will clutter the design

```html
<!DOCTYPE html>
<html lang="en">
<head>
<meta charset="utf-8">
<title>Engine Oil Label – 750ml</title>
<link rel="stylesheet" href="https://fonts.googleapis.com/css2?family=Kanit:ital,wght@0,600;1,800&family=Open+Sans:ital,wght@0,400;0,600;1,400&display=swap">
<style>
  :root {
    --stage: #000000;
    --label-dark: #232324;
    --label-dark-edge: #303031;
    --cream-light: #f3efe8;
    --cream-mid: #ddd5c8;
    --gold-dark: #6b4a26;
    --gold-light: #e9d8bd;
    --beige-type: #c8b898;
    --copper: #b5784a;
    --art-light: #9a8e7c;
    --art-mid: #5a5248;
    --art-dark: #2a2826;
    --white: #ffffff;
  }
  html, body {
    margin: 0;
    padding: 0;
    width: 1200px;
    height: 1200px;
    overflow: hidden;
    background: var(--stage);
  }
  .canvas {
    position: relative;
    width: 1200px;
    height: 1200px;
  }
  .label {
    position: absolute;
    left: 354px;
    top: 276px;
    width: 485px;
    height: 538px;
  }
  .brand-name {
    font-family: "Kanit", sans-serif;
    font-weight: 600;
    fill: var(--copper);
  }
  .product-title {
    font-family: "Kanit", sans-serif;
    font-weight: 800;
    font-style: italic;
    fill: var(--beige-type);
  }
  .product-description {
    font-family: "Kanit", sans-serif;
    font-weight: 800;
    font-style: italic;
    fill: var(--white);
  }
  .product-code {
    font-family: "Open Sans", sans-serif;
    font-weight: 600;
    fill: var(--beige-type);
    letter-spacing: 1px;
  }
  .product-type {
    font-family: "Open Sans", sans-serif;
    font-style: italic;
    fill: var(--beige-type);
  }
  .product-grade {
    font-family: "Open Sans", sans-serif;
    font-style: italic;
    fill: var(--white);
  }
  .product-size {
    font-family: "Open Sans", sans-serif;
    fill: var(--white);
  }
  .placement-note {
    position: absolute;
    left: 0;
    width: 1200px;
    top: 843px;
    margin: 0;
    text-align: center;
    font-family: "Open Sans", sans-serif;
    font-size: 22.5px;
    color: var(--white);
    letter-spacing: -0.2px;
  }
</style>
</head>
<body>
<div class="canvas">
  <svg class="label" viewBox="0 0 485 538" xmlns="http://www.w3.org/2000/svg">
    <defs>
      <clipPath id="label-shape">
        <path d="M0,204 C0,84 108,0 242.5,0 C377,0 485,84 485,204 L485,525 Q485,538 472,538 L13,538 Q0,538 0,525 Z"/>
      </clipPath>
      <linearGradient id="dark-base" x1="0" y1="0" x2="1" y2="1">
        <stop offset="0" stop-color="var(--label-dark-edge)"/>
        <stop offset="0.5" stop-color="var(--label-dark)"/>
        <stop offset="1" stop-color="var(--label-dark-edge)"/>
      </linearGradient>
      <linearGradient id="cream-top" x1="0" y1="0" x2="1" y2="1">
        <stop offset="0" stop-color="var(--cream-light)"/>
        <stop offset="1" stop-color="var(--cream-mid)"/>
      </linearGradient>
      <linearGradient id="gold-line" x1="0" y1="0" x2="1" y2="0">
        <stop offset="0" stop-color="var(--gold-dark)"/>
        <stop offset="0.45" stop-color="var(--gold-light)"/>
        <stop offset="0.7" stop-color="var(--gold-dark)"/>
        <stop offset="1" stop-color="var(--gold-light)"/>
      </linearGradient>
      <radialGradient id="artwork-tone" cx="0.6" cy="0.45" r="0.62">
        <stop offset="0" stop-color="var(--art-light)" stop-opacity="0.85"/>
        <stop offset="0.5" stop-color="var(--art-mid)" stop-opacity="0.6"/>
        <stop offset="1" stop-color="var(--art-dark)" stop-opacity="0"/>
      </radialGradient>
    </defs>

    <g clip-path="url(#label-shape)">
      <rect class="label-body" width="485" height="538" fill="url(#dark-base)"/>
      <path class="label-cap" d="M0,224 Q220,134 485,112 L485,0 L0,0 Z" fill="url(#cream-top)"/>
      <path class="cap-swoosh" d="M0,224 Q220,134 485,112" fill="none" stroke="url(#gold-line)" stroke-width="5"/>

      <rect class="product-artwork" x="0" y="280" width="250" height="258" fill="url(#artwork-tone)" role="img" aria-label="Artwork of a modern truck with its engine and transmission"/>

      <path class="base-swoosh" d="M0,504 Q260,470 485,400" fill="none" stroke="url(#gold-line)" stroke-width="4"/>
      <path class="base-swoosh-thin" d="M0,516 Q270,486 485,414" fill="none" stroke="url(#gold-line)" stroke-width="1.5" opacity="0.7"/>
    </g>

    <g class="brand">
      <circle cx="166" cy="58" r="12" fill="var(--copper)"/>
      <text class="brand-name" x="184" y="67" font-size="26">TORVAN</text>
      <text class="brand-name" x="184" y="98" font-size="26">FREIGHT</text>
    </g>

    <text class="product-title" x="258" y="236" font-size="78" text-anchor="middle" textLength="304" lengthAdjust="spacingAndGlyphs">Product</text>
    <text class="product-description" x="258" y="272" font-size="26" text-anchor="middle" textLength="308" lengthAdjust="spacingAndGlyphs">Product Discription</text>
    <text class="product-code" x="258" y="298" font-size="14" text-anchor="middle">CODE: TF-0000</text>

    <text class="product-type" x="342" y="358" font-size="21" text-anchor="middle">Engine oil</text>
    <text class="product-grade" x="342" y="410" font-size="54" text-anchor="middle" textLength="172" lengthAdjust="spacingAndGlyphs">20W-50</text>

    <text class="product-size" x="444" y="510" font-size="20" text-anchor="end">750ml</text>
  </svg>

  <p class="placement-note">IMAGE&nbsp; AND COPY FOR PLACEMENT ONLY</p>
</div>
</body>
</html>
```